Organic loose leaf tea labels hand crafted on the Great Ocean Road

We are two mums that hand craft organic loose leaf tea in our spare time. . . We are starting to get a lovely following of cafes but need to work on our retail market. We have black boxes that have our logo and name in foiled gold on the front. WE would like each tea label in a different back ground colour so that the tea is easier to identify, whilst the back label to be black background with gold text.
We are after two base labels for our new tea boxes, one label for the front with the tea name, a brief description and the ingredients. Whilst the back label needs to have information on how to make the tea, place for barcode, weight and best before. I have uploaded a file below with more detailed description.
Our box dimensions are 16cm high and 8cm across the front/back
We also need to update our business cards to reflect the new direction, moving away from the 'kraft' look. our website is www.willowandquill.com.au

Target Market(s)

women aged 25-45

Font styles to use
Other font styles liked:
• We use 'Subway Novella'

Requirements
Must have
• Minimalist feel - easy to read

```html
<!DOCTYPE html>
<html lang="en">
<head>
<meta charset="utf-8">
<title>Willow &amp; Quill — Tea Box Labels</title>
<link rel="stylesheet" href="https://fonts.googleapis.com/css2?family=Open+Sans:wght@400;600&family=Rye&family=Zilla+Slab:wght@700&display=swap">
<style>
  :root {
    --page: #e4e4e2;
    --box-dark: #121212;
    --box-mid: #262626;
    --gold: #c9a43a;
    --gold-light: #e0c463;
    --ink: #1b1b1b;
    --sage: #6e9670;
    --sage-text: #6b8f6d;
    --paper: #ffffff;
  }
  * { margin: 0; padding: 0; box-sizing: border-box; }
  html, body { width: 1200px; height: 880px; overflow: hidden; background: var(--page); }
  .canvas { position: relative; width: 1200px; height: 880px; }

  .tea-box {
    position: absolute; top: 197px; width: 264px; height: 534px;
    background: linear-gradient(100deg, var(--box-dark) 0%, var(--box-mid) 48%, var(--box-dark) 100%);
  }
  .tea-box--front { left: 297px; }
  .tea-box--back { left: 652px; }

  /* front */
  .brand-seal {
    position: absolute; left: 78px; top: 43px; width: 108px; height: 108px;
    border-radius: 50%; background: var(--gold);
    display: flex; align-items: center; justify-content: center;
  }
  .brand-seal__name {
    font-family: "Open Sans", sans-serif; font-weight: 600;
    font-size: 15px; color: var(--ink); text-align: center; line-height: 1.1;
  }
  .tagline {
    position: absolute; left: 0; right: 0; top: 161px; text-align: center;
    font-family: "Zilla Slab", serif; font-weight: 700; font-size: 10.5px;
    color: var(--gold); letter-spacing: -0.1px;
  }
  .flavour-label {
    position: absolute; left: 47px; top: 271px; width: 176px; height: 175px;
    background: var(--paper); border-radius: 4px; padding: 9px;
  }
  .flavour-label__pattern {
    width: 100%; height: 100%; background: var(--sage);
    display: flex; align-items: center; justify-content: center;
  }
  .flavour-label__disc {
    width: 118px; height: 118px; border-radius: 50%; background: var(--paper);
    display: flex; flex-direction: column; align-items: center; justify-content: center;
    text-align: center; padding: 0 8px;
  }
  .flavour-label__name {
    font-family: "Rye", serif; font-size: 16px; line-height: 1.05; color: var(--sage-text);
  }
  .flavour-label__desc {
    margin-top: 5px; font-family: "Open Sans", sans-serif; font-size: 6.4px;
    line-height: 1.35; color: var(--sage-text);
  }

  /* back */
  .info-frame { position: absolute; left: 0; top: 0; }
  .back-seal {
    position: absolute; left: 98px; top: 100px; width: 72px; height: 72px;
    border-radius: 50%; background: var(--gold);
    display: flex; align-items: center; justify-content: center;
  }
  .back-seal__name {
    font-family: "Open Sans", sans-serif; font-weight: 600; font-size: 10.5px;
    color: var(--ink); text-align: center; line-height: 1.1;
  }
  .info {
    position: absolute; left: 55px; width: 156px; text-align: center;
    font-family: "Open Sans", sans-serif; color: var(--gold);
  }
  .info--claims { top: 182px; font-size: 12.5px; line-height: 1.25; }
  .info--story { top: 227px; font-size: 9.4px; line-height: 1.28; }
  .info--meta {
    top: 348px; display: flex; gap: 26px; justify-content: flex-start;
    padding-left: 11px; font-size: 9.4px;
  }
  .info--contact { top: 371px; font-size: 7.6px; line-height: 1.52; left: 50px; width: 166px; }
  .social-dot {
    display: inline-block; width: 6px; height: 6px; background: var(--gold);
    margin-right: 3px; vertical-align: -0.5px;
  }
</style>
</head>
<body>
<main class="canvas">

  <section class="tea-box tea-box--front" aria-label="Front of tea box">
    <div class="brand-seal"><span class="brand-seal__name">willow &amp;<br>quill</span></div>
    <p class="tagline">hand crafted organic loose leaf tea</p>

    <div class="flavour-label">
      <div class="flavour-label__pattern" role="img" aria-label="Sage green decorative pattern with ornamental border around the tea name">
        <div class="flavour-label__disc">
          <h1 class="flavour-label__name">English<br>Breakfast</h1>
          <p class="flavour-label__desc">The quintessential ‘British cup of tea’, a classically strong &amp; full bodied blend. Ingredients: English breakfast tea</p>
        </div>
      </div>
    </div>
  </section>

  <section class="tea-box tea-box--back" aria-label="Back of tea box">
    <svg class="info-frame" width="264" height="534" viewBox="0 0 264 534" aria-hidden="true">
      <path d="M59 145 Q51 145 51 153 V435 Q51 442 58 442 H209 Q216 442 216 435 V153 Q216 145 208 145 H177 A44 44 0 0 0 91 145 Z"
            fill="none" stroke="var(--gold)" stroke-width="1.3"/>
    </svg>
    <div class="back-seal"><span class="back-seal__name">willow &amp;<br>quill</span></div>

    <div class="info info--claims">organic<br>vegan<br>no added sugar</div>
    <p class="info info--story">I’m hand crafted along the Great Ocean Road from local and imported organic ingredients and I’m super proud to be Australian owned. Directions: place 1 to 2 teaspoons in a medium sized pot add water 95 degrees, allow to infuse for 2 to 3 minutes.</p>
    <div class="info info--meta"><span>Weight:</span><span>Best before:</span></div>
    <address class="info info--contact" style="font-style:normal">
      www.willowandquill.com.au<br>
      <span class="social-dot"></span>willowandquilltea &nbsp;<span class="social-dot"></span>wandqtea<br>
      <span class="social-dot"></span>leafandkettle<br>
      hello@willowandquill.com.au<br>
      Packaged at 1457 Coastal Way,<br>
      Marrowbay VIC 3299
    </address>
  </section>

</main>
</body>
</html>
```